Small holiday retreat needs new Internet launch

"The Evolution from a Ruin into a Holiday Retreat.
My wife and I rebuilt a small farm in a remote village into a little holiday retreat. Though close to the Baltic Sea, we want to attract people with the desire to spend some days in a secluded place. Though remote it offers some luxury - and time ticks slower.
This summer was our third season and we want to adapt our Internet pages. Look at our business card - we want to keep this style.
It should be a bit mystic and should not attract the bargain hunter.
We realized that in summer our name "Wiesenlicht" (ie sunny hill) does not fit for the dark part of the year - then it is more like "Hollow Moor Gate".
We have a guesthouse (the former stable) and two tiny houses. Additionally, we have lavatory with sauna in the rebuilt barn and a fitness room.
On our farm live a few animals (dog, cats, chicken, bees) + wild visitors.
Our current home page is www.wiesenlicht-example.net
A few pictures are on Google Maps and I can share more in Google Drive.
The final homepage should also offer translations into English, French, Dutch.
Better and consistent fonts.
No "galery" but more "four seasons".

Target Market(s)

Individual travellers - not just from Germany!

Industry/Entity Type

Tourism

Coding

Coded - Design and coding required

Number of Pages Required

4 page

Font styles to use
Script

Colors
FFC000
F8CF3A
FAE287
FDF2CF
FEFAEE

Requirements
Must have
• A "mystic" and romantic appearance.
Nice to have
• See my comments.

```html
<!DOCTYPE html>
<html lang="en">
<head>
<meta charset="utf-8">
<title>Wiesenlicht – Rest and Relaxation</title>
<link rel="stylesheet" href="https://fonts.googleapis.com/css2?family=Questrial&family=Lexend:wght@500;600&family=Dancing+Script:wght@500&display=swap">
<style>
:root{
  --dark:#2f2e34;
  --dark-card:#3b3a41;
  --gold:#f2bb4c;
  --gold-soft:#f5c75f;
  --text:#333238;
  --muted:#5a5960;
  --light:#f1f1f1;
  --white:#ffffff;
}
*{box-sizing:border-box;margin:0;padding:0}
html,body{width:1200px;height:4168px;overflow:hidden}
body{font-family:"Questrial",sans-serif;color:var(--text);background:var(--white)}
section,header,footer,.topbar{position:relative;width:1200px;overflow:hidden}
.abs{position:absolute}
.heading{font-family:"Lexend",sans-serif;font-weight:600}
.script{font-family:"Dancing Script",cursive;font-weight:500}
.btn{position:absolute;display:flex;align-items:center;justify-content:center;gap:6px;font-family:"Lexend",sans-serif;font-weight:600;font-size:13px;text-transform:uppercase;color:var(--dark);background:var(--gold);border-radius:30px}
.btn svg{width:12px;height:12px}

.topbar{height:52px;background:var(--dark);color:#e8e8ea;font-size:15px}
.topbar .item{position:absolute;top:0;height:52px;display:flex;align-items:center;gap:8px;white-space:nowrap}
.topbar svg{width:15px;height:15px;fill:var(--gold)}
.social{position:absolute;display:flex;gap:20px}
.social span{width:14px;height:14px;border-radius:50%;background:currentColor;display:block}

header{height:116px;background:var(--white)}
.brand{position:absolute;left:100px;top:30px;display:flex;align-items:center;gap:10px;color:var(--gold);font-size:34px}
.brand .dot{width:52px;height:52px;border-radius:50%;background:var(--gold)}
.brand small{display:block;font-size:14px;line-height:1}
.nav{position:absolute;top:50px;left:420px;display:flex;gap:34px;font-size:13px;text-transform:uppercase;color:var(--text)}
.nav .active{color:var(--gold)}
.nav .lang{display:flex;align-items:center;gap:6px}
.nav .flag{width:20px;height:12px;background:#7a86b8;display:block}

.hero{height:560px;background:linear-gradient(100deg,#5b4535 0%,#3c2d25 45%,#2a211d 100%)}
.hero .photo{position:absolute;inset:0;background:radial-gradient(circle at 28% 45%,rgba(190,140,90,.45),transparent 45%),radial-gradient(circle at 40% 10%,rgba(90,120,190,.5),transparent 25%)}
.hero .tag{left:557px;top:178px;font-size:28px;color:var(--gold-soft)}
.hero h1{position:absolute;left:557px;top:220px;font-family:"Lexend",sans-serif;font-weight:600;font-size:56px;color:var(--white);letter-spacing:.5px;white-space:nowrap}
.booking{position:absolute;left:542px;top:320px;width:559px;height:162px;background:rgba(74,58,48,.85)}
.booking label{position:absolute;top:18px;font-size:13px;color:#f2f2f2}
.field{position:absolute;top:47px;height:41px;background:var(--white);border-radius:2px;font-size:14px;color:#444;display:flex;align-items:center;justify-content:space-between;padding:0 10px}
.field svg{width:13px;height:13px;fill:#555}
.booking .search{left:375px;top:99px;width:174px;height:40px;border-radius:2px;font-size:13px}
.hero .curve{position:absolute;left:0;bottom:0}

.welcome{height:566px}
.welcome .mark{left:286px;top:62px;width:30px;height:30px;border-radius:50%;background:var(--gold)}
.welcome .eyebrow{position:absolute;left:100px;width:402px;top:110px;text-align:center;font-family:"Lexend",sans-serif;font-weight:600;font-size:13px;letter-spacing:1px}
.welcome h2{position:absolute;left:100px;width:402px;top:133px;text-align:center;font-size:38px;line-height:46px;color:var(--text)}
.welcome p{position:absolute;left:100px;width:402px;top:229px;text-align:center;font-size:16px;line-height:24px;color:var(--muted)}
.welcome .more{left:208px;top:414px;width:166px;height:50px}
.pic{position:absolute;background:linear-gradient(180deg,#4d6a2c 0%,#6f8a3a 40%,#d7a24a 70%,#5f6d33 100%)}

.accommodation{height:706px;background:var(--white)}
.accommodation .band{position:absolute;left:0;top:0;width:1200px;height:401px;background:var(--dark)}
.accommodation h2{position:absolute;top:64px;width:1200px;text-align:center;font-size:40px;color:var(--white)}
.card{position:absolute;top:174px;width:318px;height:448px;background:var(--dark-card);color:var(--white);text-align:center}
.card .img{height:227px}
.card h3{margin-top:25px;font-family:"Lexend",sans-serif;font-weight:600;font-size:22px}
.card p{margin:18px auto 0;width:270px;font-size:16px;line-height:23px;color:#e6e6e8}
.card .outline{left:50%;transform:translateX(-50%);top:380px;width:140px;height:42px;background:transparent;border:2px solid var(--gold);color:var(--gold)}

.testimonials{height:620px;background:var(--light)}
.tbox{position:absolute;left:99px;top:71px;width:1002px;height:473px;background:var(--white)}
.tpanel{position:absolute;left:0;top:0;width:316px;height:473px;background:var(--gold-soft);overflow:hidden}
.tpanel .ring{position:absolute;width:260px;height:260px;border-radius:50%;border:44px solid rgba(255,255,255,.22)}
.tpanel .script{position:absolute;width:316px;top:190px;text-align:center;font-size:32px;color:var(--white)}
.tpanel h2{position:absolute;width:316px;top:225px;text-align:center;font-size:38px;color:var(--white)}
.quote{position:absolute;top:40px;width:290px;text-align:center}
.quote .mk{font-family:"Lexend",sans-serif;font-size:90px;line-height:70px;height:50px;color:#c9c8cc}
.quote p{margin-top:12px;font-size:16px;line-height:24px;color:var(--muted)}
.stars{margin-top:14px;display:flex;justify-content:center;gap:3px}
.stars svg{width:17px;height:17px;fill:#f4a13b}
.avatar{margin:14px auto 0;width:76px;height:76px;border-radius:50%;background:linear-gradient(#c7c9cf,#8b8d94)}
.quote .name{margin-top:6px;font-family:"Lexend",sans-serif;font-weight:600;font-size:17px;color:var(--text)}

.contact{height:472px;background:linear-gradient(180deg,#3a3330 0%,#221f20 60%,#151416 100%)}
.contact .eyebrow{position:absolute;top:82px;width:1200px;text-align:center;font-family:"Lexend",sans-serif;font-weight:500;font-size:19px;color:var(--white);letter-spacing:1px}
.contact h2{position:absolute;top:104px;width:1200px;text-align:center;font-size:38px;color:var(--white)}
.input{position:absolute;background:var(--white);border:1px solid #ccc;font-size:16px;color:#444;padding:8px 10px}
.contact .submit{left:517px;top:339px;width:165px;height:49px}

.map{height:563px;background:#ececec}
.map .tiles{position:absolute;inset:0;background:linear-gradient(160deg,#e9e9e9,#dcdcdc 60%,#ececec)}
.pin{position:absolute;left:609px;top:205px;width:20px;height:28px}
.ccard{position:absolute;left:99px;top:84px;width:310px;height:317px;background:var(--gold-soft);color:var(--dark)}
.ccard h2{position:absolute;left:14px;top:52px;font-size:38px}
.crow{position:absolute;left:14px;width:290px;display:flex;gap:8px;font-family:"Lexend",sans-serif;font-weight:500;font-size:15px;line-height:22px}
.crow svg{flex:none;width:15px;height:15px;margin-top:4px;fill:var(--dark)}
.map .curve{position:absolute;left:0;bottom:0}

footer{height:513px;background:var(--dark);color:#e6e6e8}
.signup{position:absolute;left:184px;top:47px;font-family:"Lexend",sans-serif;font-weight:500;font-size:24px;color:var(--white)}
.subscribe{position:absolute;left:555px;top:37px;width:460px;height:48px;background:var(--white);border-radius:30px;display:flex;align-items:center;padding-left:16px;gap:8px;font-size:14px;color:#888}
.subscribe svg{width:15px;height:15px;fill:#888}
.subscribe .btn{right:0;top:0;width:132px;height:48px;font-size:13px}
.rule{position:absolute;left:97px;width:1004px;height:1px;background:#55545b}
.fbrand{position:absolute;left:100px;top:222px;display:flex;align-items:center;gap:10px;color:var(--gold);font-size:34px}
.fbrand .dot{width:52px;height:52px;border-radius:50%;background:var(--gold)}
.fbrand small{display:block;font-size:14px;line-height:1}
.col{position:absolute;top:176px}
.col h4{font-family:"Lexend",sans-serif;font-weight:600;font-size:13px;letter-spacing:1.5px;color:var(--gold);margin-bottom:20px}
.col li{list-style:none;font-size:15px;line-height:37px;display:flex;align-items:center;gap:9px}
.col li::before{content:"›";color:var(--gold);font-size:18px}
.copy{position:absolute;top:472px;width:1200px;text-align:center;font-size:15px;color:#c9c9cc}
.copy span{color:var(--gold)}
.totop{position:absolute;left:1053px;top:458px;width:48px;height:48px;border-radius:50%;background:var(--gold);display:flex;align-items:center;justify-content:center}
.totop svg{width:18px;height:18px;stroke:var(--dark);fill:none;stroke-width:2.5}
</style>
</head>
<body>

<div class="topbar">
  <div class="item" style="left:100px"><svg viewBox="0 0 16 16"><path d="M1 3h14v10H1z"/><path d="M1 3l7 6 7-6" stroke="#2f2e34" fill="none"/></svg>post@wiesenlicht-example.de</div>
  <div class="item" style="left:360px"><svg viewBox="0 0 16 16"><path d="M3 1l3 3-2 2c1 2 3 4 5 5l2-2 3 3-2 3C7 15 1 9 1 3z"/></svg>+49 157 000 481 26</div>
  <div class="social" style="left:1014px;top:19px;color:#e8e8ea" aria-label="Social links"><span></span><span></span><span></span></div>
</div>

<header>
  <div class="brand"><span class="dot"></span><div><small>Urlaub auf dem</small>Wiesenlicht</div></div>
  <nav class="nav">
    <span class="active">Home</span><span>About us</span><span>Accommodation</span><span>Bookings &amp; Calendar</span><span>Contact</span><span class="lang"><i class="flag"></i>Eng ▾</span>
  </nav>
</header>

<section class="hero">
  <div class="photo" role="img" aria-label="Evening photo of a softly lit guest bedroom with a large decorative emblem overlay"></div>
  <div class="abs tag script">We have turned our old farm into a place of</div>
  <h1>Rest and Relaxation</h1>
  <div class="booking">
    <label style="left:13px">Arrival</label><label style="left:195px">Departure</label><label style="left:375px">Persons</label>
    <div class="field" style="left:13px;width:173px">Oct 05, 22<svg viewBox="0 0 14 14"><path d="M1 3h12v10H1zM3 1h2v3H3zM9 1h2v3H9z"/></svg></div>
    <div class="field" style="left:195px;width:173px">Oct 06, 22<svg viewBox="0 0 14 14"><path d="M1 3h12v10H1zM3 1h2v3H3zM9 1h2v3H9z"/></svg></div>
    <div class="field" style="left:375px;width:174px">01<svg viewBox="0 0 14 14"><path d="M3 5l4 4 4-4" stroke="#555" stroke-width="1.6" fill="none"/></svg></div>
    <div class="btn search">Search</div>
  </div>
  <svg class="curve" width="1200" height="100" viewBox="0 0 1200 100"><path d="M0 50 Q600 130 1200 45 V100 H0Z" fill="#fff"/></svg>
</section>

<section class="welcome">
  <div class="abs mark"></div>
  <div class="eyebrow">WELCOME TO THE</div>
  <h2 class="heading">Wiesenlicht in Beautiful Heidemark</h2>
  <p>Welcome to the Wiesenlicht in beautiful Heidemark. With great attention to detail, we have turned our old farm into a place of rest and relaxation. Whether in the tiny house "Ambra" or the holiday apartments "Nordwind" and "Morgenrot", in all of our accommodations we attach great importance</p>
  <div class="btn more">Read more <svg viewBox="0 0 12 12"><path d="M1 6h9M6 2l4 4-4 4" stroke="#2f2e34" stroke-width="1.6" fill="none"/></svg></div>
  <div class="pic" style="left:535px;top:85px;width:274px;height:348px" role="img" aria-label="Yellow farmhouse with red roof behind green trees"></div>
  <div class="pic" style="left:826px;top:129px;width:275px;height:349px" role="img" aria-label="Yellow farmhouse facade with garden seating"></div>
</section>

<section class="accommodation">
  <div class="band"></div>
  <h2 class="heading">Accommodation</h2>
  <div class="card" style="left:97px">
    <div class="img" style="background:linear-gradient(160deg,#c98a2a,#7a4a22 60%,#a97b48)" role="img" aria-label="Loft bedroom with wooden furniture and brick wall"></div>
    <h3>Design-Refuge "Nordwind"</h3>
    <p>Historical elements with contemporary design characterize this feel-good loft.</p>
    <div class="btn outline">More info <svg viewBox="0 0 12 12"><path d="M1 6h9M6 2l4 4-4 4" stroke="#f2bb4c" stroke-width="1.6" fill="none"/></svg></div>
  </div>
  <div class="card" style="left:441px">
    <div class="img" style="background:linear-gradient(170deg,#d8d6d2,#a9a49c 55%,#5f5a55)" role="img" aria-label="Bright attic room with skylight and pendant lamp"></div>
    <h3>Design-Refuge "Morgenrot"</h3>
    <p>Morgenrot shows the love for clear but warm simplicity.</p>
    <div class="btn outline">More info <svg viewBox="0 0 12 12"><path d="M1 6h9M6 2l4 4-4 4" stroke="#f2bb4c" stroke-width="1.6" fill="none"/></svg></div>
  </div>
  <div class="card" style="left:784px">
    <div class="img" style="background:linear-gradient(150deg,#f3c9a0,#d98a55 55%,#b8643a)" role="img" aria-label="Warm lit tiny house interior with fireplace and window"></div>
    <h3>Tiny House "Mondlicht"</h3>
    <p>The Mondlicht is all about modern, cozy comfort.</p>
    <div class="btn outline">More info <svg viewBox="0 0 12 12"><path d="M1 6h9M6 2l4 4-4 4" stroke="#f2bb4c" stroke-width="1.6" fill="none"/></svg></div>
  </div>
</section>

<section class="testimonials">
  <div class="tbox">
    <div class="tpanel">
      <div class="ring" style="left:-80px;top:-80px"></div>
      <div class="ring" style="left:160px;top:330px"></div>
      <div class="script">Client</div>
      <h2 class="heading">Testimonials</h2>
    </div>
    <div class="quote" style="left:356px">
      <div class="mk">“</div>
      <p>Lorem ipsum dolor sit at, constetur adipiscing elit. Donec magna massa, vestibulum et tincidunt in, tempor vitae tellus. Phasellus conlis tempus tincidunt. Quisque nunc ligula, euimod quis iaculis sit amet, rhoncus in lectus.</p>
      <div class="stars"><svg viewBox="0 0 20 20"><path d="M10 1l2.6 6 6.4.5-4.9 4.2 1.5 6.3L10 14.6 4.4 18l1.5-6.3L1 7.5 7.4 7z"/></svg><svg viewBox="0 0 20 20"><path d="M10 1l2.6 6 6.4.5-4.9 4.2 1.5 6.3L10 14.6 4.4 18l1.5-6.3L1 7.5 7.4 7z"/></svg><svg viewBox="0 0 20 20"><path d="M10 1l2.6 6 6.4.5-4.9 4.2 1.5 6.3L10 14.6 4.4 18l1.5-6.3L1 7.5 7.4 7z"/></svg><svg viewBox="0 0 20 20"><path d="M10 1l2.6 6 6.4.5-4.9 4.2 1.5 6.3L10 14.6 4.4 18l1.5-6.3L1 7.5 7.4 7z"/></svg><svg viewBox="0 0 20 20"><path d="M10 1l2.6 6 6.4.5-4.9 4.2 1.5 6.3L10 14.6 4.4 18l1.5-6.3L1 7.5 7.4 7z"/></svg></div>
      <div class="avatar" role="img" aria-label="Guest portrait"></div>
      <div class="name">Jonas</div>
    </div>
    <div class="quote" style="left:692px">
      <div class="mk">“</div>
      <p>Lorem ipsum dolor sit at, constetur adipiscing elit. Donec magna massa, vestibulum et tincidunt in, tempor vitae tellus. Phasellus conlis tempus tincidunt. Quisque nunc ligula, euimod quis iaculis sit amet, rhoncus in lectus.</p>
      <div class="stars"><svg viewBox="0 0 20 20"><path d="M10 1l2.6 6 6.4.5-4.9 4.2 1.5 6.3L10 14.6 4.4 18l1.5-6.3L1 7.5 7.4 7z"/></svg><svg viewBox="0 0 20 20"><path d="M10 1l2.6 6 6.4.5-4.9 4.2 1.5 6.3L10 14.6 4.4 18l1.5-6.3L1 7.5 7.4 7z"/></svg><svg viewBox="0 0 20 20"><path d="M10 1l2.6 6 6.4.5-4.9 4.2 1.5 6.3L10 14.6 4.4 18l1.5-6.3L1 7.5 7.4 7z"/></svg><svg viewBox="0 0 20 20"><path d="M10 1l2.6 6 6.4.5-4.9 4.2 1.5 6.3L10 14.6 4.4 18l1.5-6.3L1 7.5 7.4 7z"/></svg><svg viewBox="0 0 20 20"><path d="M10 1l2.6 6 6.4.5-4.9 4.2 1.5 6.3L10 14.6 4.4 18l1.5-6.3L1 7.5 7.4 7z"/></svg></div>
      <div class="avatar" role="img" aria-label="Guest portrait"></div>
      <div class="name">Clara Berg</div>
    </div>
  </div>
</section>

<section class="contact" role="img" aria-label="Dusk scene of dune grass in silhouette">
  <div class="eyebrow">CONTACT US</div>
  <h2 class="heading">Get In Touch</h2>
  <div class="input" style="left:225px;top:171px;width:368px;height:40px">Name</div>
  <div class="input" style="left:225px;top:226px;width:368px;height:39px">Email</div>
  <div class="input" style="left:225px;top:274px;width:368px;height:44px">Regarding</div>
  <div class="input" style="left:606px;top:171px;width:369px;height:147px">Your Message</div>
  <div class="btn submit">Submit now <svg viewBox="0 0 12 12"><path d="M1 6h9M6 2l4 4-4 4" stroke="#2f2e34" stroke-width="1.6" fill="none"/></svg></div>
</section>

<section class="map">
  <div class="tiles" role="img" aria-label="Map of the surrounding countryside near the coast"></div>
  <svg class="pin" viewBox="0 0 20 28"><path d="M10 0C4.5 0 0 4.5 0 10c0 7 10 18 10 18s10-11 10-18C20 4.5 15.5 0 10 0z" fill="#e0332b"/><circle cx="10" cy="10" r="3.5" fill="#8a1b17"/></svg>
  <div class="ccard">
    <h2 class="heading">Contact Us</h2>
    <div class="crow" style="top:118px"><svg viewBox="0 0 16 16"><path d="M8 0C4.7 0 2 2.7 2 6c0 4.5 6 10 6 10s6-5.5 6-10c0-3.3-2.7-6-6-6zm0 8.5A2.5 2.5 0 118 3.5a2.5 2.5 0 010 5z"/></svg>Stiller Grund 7, 18000 Feldhausen, Germany</div>
    <div class="crow" style="top:186px"><svg viewBox="0 0 16 16"><path d="M3 1l3 3-2 2c1 2 3 4 5 5l2-2 3 3-2 3C7 15 1 9 1 3z"/></svg>+49 157 000 481 26</div>
    <div class="crow" style="top:231px"><svg viewBox="0 0 16 16"><path d="M1 3h14v10H1z"/><path d="M1 3l7 6 7-6" stroke="#f5c75f" fill="none"/></svg>post@wiesenlicht-example.de</div>
  </div>
  <svg class="curve" width="1200" height="100" viewBox="0 0 1200 100"><path d="M0 92 Q600 -60 1200 90 V100 H0Z" fill="#2f2e34"/></svg>
</section>

<footer>
  <div class="signup">SIGN UP FOR LATEST UPDATE</div>
  <div class="subscribe"><svg viewBox="0 0 16 16"><path d="M1 3h14v10H1z"/><path d="M1 3l7 6 7-6" stroke="#fff" fill="none"/></svg>Enter email address<div class="btn">Subscribe <svg viewBox="0 0 12 12"><path d="M1 6h9M6 2l4 4-4 4" stroke="#2f2e34" stroke-width="1.6" fill="none"/></svg></div></div>
  <div class="rule" style="top:131px"></div>
  <div class="fbrand"><span class="dot"></span><div><small>Urlaub auf dem</small>Wiesenlicht</div></div>
  <div class="col" style="left:407px"><h4>QUICK LINKS</h4><ul><li>Home</li><li>About us</li><li>Accommodation</li><li>Bookings &amp; calendar</li><li>Contact</li></ul></div>
  <div class="col" style="left:650px"><h4>ACCOMMODATION</h4><ul><li>Design-Refuge "Nordwind"</li><li>Design-Refuge "Morgenrot"</li><li>Tiny House "Mondlicht"</li><li>Tiny House "Ambra"</li></ul></div>
  <div class="col" style="left:956px"><h4>FOLLOW US</h4></div>
  <div class="social" style="left:956px;top:215px;color:#e6e6e8" aria-label="Social links"><span></span><span></span><span></span></div>
  <div class="rule" style="top:447px"></div>
  <div class="copy">© 2022 <span>Wiesenlicht</span>. All right reserved</div>
  <div class="totop"><svg viewBox="0 0 18 18"><path d="M3 12l6-6 6 6"/></svg></div>
</footer>

</body>
</html>
```